Vel Norra A4 paper and card metallic new packaging

Vel Norra New Packaging Brief
We need a CLASSIC packaging design which wraps around the bottom left side of the product (A4 card) in the shape of a square (front & back) for an existing brand name call Vel Norra. This is then covered in a polybag. This needs to display the most important detail about the product on the FRONT and then the other information on the back.
See images attached of some ideas
The packaging needs to be CLEAN and simple to portray the fact the product is of a Premium Luxurious quality.
It is sold in a store where it sits on a shelf so we need the following information portrayed very clearly so the consumer can see it straight away and know what the product is:
The below points need to be shown on the FRONT of the packaging - Information is listed in order of importance.
1.Premium Luxurious Card
2. Metallic
3. A4
4.The Colour (eg, Silver)
5.25 Pack
6. Logo – this can be small

These need to be shown on the BACK of the packaging - Information is listed in order of importance.
1.PREMIUM Luxurious Card
2.
• Ideal for card making for all occasions
• Invitations for all Celebrations
• Creative card & paper for presentations
3. Acid free
4. Made in china
5. Logo – this can be small
6.Barcode

Background
Vel Norra is a brand which sells PREMIUM Luxurious Paper and card stock which can be used for card making, invites, presentations. The colour range is approx. 24 colours and it comes in metallic and weave. It includes the following
*A4 Card 260gsm & paper 120gsm
*DL & C6 envelopes 120gsm

PLEASE READ ALL UPLOADED FILE NAMES.

Target Market(s)

Office supply and invitation market

Industry/Entity Type

Store

Requirements
Must have
• Most important is to have a style of packaging that suits and displays the product. Needs to be fresh and clean packaging but also show quality and show the actual product.
• Font should be simple, easy to read, clear so consumers can read what the product is straight away.
• Colours – can match the logo but we are open to other ideas as well.
• The colour range of the card we sell is 24 different colours so the actual packaging needs to match all colours and stand out.

```html
<!DOCTYPE html>
<html lang="en">
<head>
<meta charset="utf-8">
<title>Vel Norra Premium Card Packaging</title>
<link rel="stylesheet" href="https://fonts.googleapis.com/css2?family=Oswald:wght@300;400&family=Roboto+Condensed:wght@400&display=swap">
<style>
  :root {
    --page: #ffffff;
    --pack: #000000;
    --teal: #2aa7bd;
    --grey: #8c8c8c;
    --grey-light: #9a9a9a;
    --seal: #b3121c;
    --seal-light: #d8303a;
    --seal-dark: #7a0b12;
    --badge: #cfcfcf;
  }
  * { margin: 0; padding: 0; box-sizing: border-box; }
  html, body {
    width: 1200px; height: 355px; overflow: hidden;
    background: var(--page);
  }
  .canvas { position: relative; width: 1200px; height: 355px; }

  .pack {
    position: absolute; background: var(--pack); overflow: hidden;
    font-family: "Oswald", "Arial Narrow", sans-serif;
  }
  .pack--front { left: 42px; top: 30px; width: 294px; height: 295px; border-radius: 14px; }
  .pack--band  { left: 397px; top: 76px; width: 769px; height: 194px; }

  .gold-line { position: absolute; left: 0; top: 0; }

  .brand {
    position: absolute; color: var(--teal);
    font-weight: 300; letter-spacing: 1px; white-space: nowrap;
  }
  .pack--front .brand { left: 60px; width: 200px; top: 38px; text-align: center; font-size: 38px; }
  .pack--band .brand  { left: 20px; width: 230px; top: 66px; text-align: center; font-size: 44px; }

  .title  { position: absolute; color: var(--teal); font-weight: 300; line-height: 1; }
  .spec   { position: absolute; color: var(--grey); font-weight: 300; line-height: 1; white-space: nowrap; }
  .size   { position: absolute; color: var(--grey); font-weight: 300; line-height: 1; }
  .colour { position: absolute; color: var(--grey); font-weight: 300; line-height: 1; white-space: nowrap; }
  .features {
    position: absolute; color: var(--grey-light); list-style: none;
    font-family: "Roboto Condensed", "Arial Narrow", sans-serif; line-height: 1.3;
    white-space: nowrap;
  }

  .pack--front .title    { left: 14px; top: 118px; font-size: 36px; }
  .pack--front .spec     { left: 14px; top: 166px; font-size: 19px; }
  .pack--front .size     { left: 12px; top: 194px; font-size: 46px; }
  .pack--front .colour   { left: 78px; top: 207px; font-size: 25px; }
  .pack--front .features { left: 14px; top: 253px; font-size: 6.6px; }

  .pack--band .title    { left: 284px; top: 26px; font-size: 42px; }
  .pack--band .spec     { left: 284px; top: 74px; font-size: 19px; }
  .pack--band .size     { left: 282px; top: 104px; font-size: 54px; }
  .pack--band .colour   { left: 350px; top: 118px; font-size: 28px; }
  .pack--band .features { left: 284px; top: 163px; font-size: 6.8px; }
  .pack--band .features li { display: inline; }

  .seal-art {
    position: absolute;
    background: radial-gradient(ellipse at 45% 40%, var(--seal-light) 0%, var(--seal) 50%, var(--seal-dark) 100%);
    border-radius: 10px;
  }
  .pack--front .seal-art { left: 186px; top: 110px; width: 72px; height: 118px; }
  .pack--band .seal-art  { left: 538px; top: 4px; width: 150px; height: 190px; border-radius: 10px 10px 0 0; }

  .cert-badge { position: absolute; background: var(--badge); border-radius: 4px; }
  .pack--front .cert-badge { left: 220px; top: 245px; width: 34px; height: 34px; }
  .pack--band .cert-badge  { left: 718px; top: 140px; width: 32px; height: 38px; }
</style>
</head>
<body>
<main class="canvas">

  <section class="pack pack--front" aria-label="Front panel">
    <svg class="gold-line" width="294" height="295" viewBox="0 0 294 295" aria-hidden="true">
      <defs>
        <linearGradient id="goldFront" x1="0" x2="1" y1="0" y2="0">
          <stop offset="0" stop-color="#c9a45c" stop-opacity="0"/>
          <stop offset="0.4" stop-color="#f3dfae"/>
          <stop offset="0.7" stop-color="#c9a45c"/>
          <stop offset="1" stop-color="#c9a45c" stop-opacity="0.2"/>
        </linearGradient>
      </defs>
      <path d="M0 104 C 90 94, 180 96, 294 100" stroke="url(#goldFront)" stroke-width="2.2" fill="none"/>
    </svg>

    <div class="brand">Vel Norra</div>

    <h1 class="title">PREMIUM</h1>
    <p class="spec">Card 260gsm / 25 pack</p>
    <p class="size">A4</p>
    <p class="colour">Silver Grey</p>

    <ul class="features">
      <li>Premium Metallic card</li>
      <li>Matching envelopes</li>
      <li>Suitable for most laser and inkjet prints*</li>
      <li>Perfect for office, school, craft or invitations projects</li>
    </ul>

    <div class="seal-art" role="img" aria-label="Red wax seal with ribbon marking the premium range"></div>
    <div class="cert-badge" role="img" aria-label="Forest certification badge"></div>
  </section>

  <section class="pack pack--band" aria-label="Wrap band">
    <svg class="gold-line" width="769" height="194" viewBox="0 0 769 194" aria-hidden="true">
      <defs>
        <linearGradient id="goldBand" x1="0" x2="0" y1="0" y2="1">
          <stop offset="0" stop-color="#c9a45c" stop-opacity="0.3"/>
          <stop offset="0.45" stop-color="#f3dfae"/>
          <stop offset="1" stop-color="#c9a45c" stop-opacity="0.4"/>
        </linearGradient>
      </defs>
      <path d="M258 0 C 253 60, 253 130, 258 194" stroke="url(#goldBand)" stroke-width="2.4" fill="none"/>
    </svg>

    <div class="brand">Vel Norra</div>

    <h2 class="title">PREMIUM</h2>
    <p class="spec">Card 260gsm / 25 pack</p>
    <p class="size">A4</p>
    <p class="colour">Silver Grey</p>

    <ul class="features">
      <li>Premium Metallic card&nbsp;&nbsp;/&nbsp;&nbsp;</li>
      <li>Matching envelopes&nbsp;&nbsp;/&nbsp;&nbsp;</li>
      <li>Suitable for most laser and inkjet prints*</li><br>
      <li>Perfect for office, school, craft or invitations projects</li>
    </ul>

    <div class="seal-art" role="img" aria-label="Large red wax seal with ribbon marking the premium range"></div>
    <div class="cert-badge" role="img" aria-label="Forest certification badge"></div>
  </section>

</main>
</body>
</html>
```